Heron valley RV Resort business card

I need a design card for the logo I just had made on here. I will provide it and please make some cool designs, thank you.

I would like the card to have
- phone number (865-318-2967)
- email ( heronvalleyrv@pinemail.com)
- address to the park ( 5186 Quarry Gate Loop rd, Maryville, TN) ZIP: 37429
on the back for double sided id like some lines for writing on. thanks

please follow the logo we provided in the files, I can provide the photoshop file if you need it.

please note this is in the Smokey mountains of Tennessee

Target Market(s)

cabin/rv rentals

Industry/Entity Type

rv/campground/cabin rentals

Contact Information for Business Card

address/email/phone number I added details in brief

Requirements
Must have
• on the back add a bear or something cool

```html
<!DOCTYPE html>
<html lang="en">
<head>
<meta charset="utf-8">
<title>Heron valley RV Resort – Business Card</title>
<link rel="stylesheet" href="https://fonts.googleapis.com/css2?family=EB+Garamond:wght@400;500&display=swap">
<style>
  :root {
    --backdrop: #c2c2c2;
    --paper: #ffffff;
    --charcoal: #363636;
    --gold: #b38b3a;
    --gold-deep: #8f6b2a;
    --gold-soft: rgba(179,139,58,0.42);
  }
  * { box-sizing: border-box; margin: 0; padding: 0; }
  html, body {
    width: 1200px; height: 848px; overflow: hidden;
    background: var(--backdrop);
  }
  .canvas {
    position: relative; width: 1200px; height: 848px;
    display: flex; justify-content: center; align-items: center; gap: 60px;
    font-family: "EB Garamond", Garamond, serif;
  }
  .card { position: relative; width: 300px; height: 510px; }
  .card-front { background: var(--paper); }
  .card-back { background: var(--charcoal); }
  .frame {
    position: absolute; inset: 16px;
    border: 1px solid var(--gold); border-radius: 20px;
  }
  .front-content {
    position: absolute; inset: 16px;
    display: flex; flex-direction: column; align-items: center;
    color: var(--gold); text-align: center;
  }
  .brand {
    margin-top: 112px;
    display: flex; flex-direction: column; align-items: center; gap: 14px;
  }
  .brand-dot {
    width: 70px; height: 70px; border-radius: 50%;
    border: 1px solid var(--gold);
  }
  .brand-name { font-size: 25px; font-weight: 500; line-height: 1.1; }
  .phone { margin-top: 96px; font-size: 24px; font-weight: 500; }
  .email { margin-top: 2px; font-size: 14.5px; }
  .address { margin-top: 22px; font-size: 15.5px; line-height: 1.2; }

  .back-lines { position: absolute; inset: 0; }
  .art-piece {
    position: absolute; border-radius: 4px;
    background: linear-gradient(90deg, rgba(143,107,42,0.15), var(--gold-soft));
  }
  .art-tree-1 { left: 172px; top: 56px;  width: 76px;  height: 40px; }
  .art-tree-2 { left: 148px; top: 114px; width: 100px; height: 42px; }
  .art-cabin  { left: 84px;  top: 166px; width: 180px; height: 158px; }
  .art-tree-3 { left: 150px; top: 336px; width: 104px; height: 40px; }
  .art-tree-4 { left: 186px; top: 390px; width: 70px;  height: 34px; }
</style>
</head>
<body>
  <main class="canvas">
    <section class="card card-front" aria-label="Business card front">
      <div class="frame"></div>
      <div class="front-content">
        <div class="brand">
          <span class="brand-dot"></span>
          <span class="brand-name">Heron valley RV Resort</span>
        </div>
        <p class="phone">Tel. 865-318-2967</p>
        <p class="email">heronvalleyrv@pinemail.com</p>
        <p class="address">5186 Quarry Gate Loop rd,<br>Maryville, TN 37429</p>
      </div>
    </section>

    <section class="card card-back" aria-label="Business card back">
      <div class="frame"></div>
      <svg class="back-lines" width="300" height="510" viewBox="0 0 300 510" aria-hidden="true">
        <g stroke="#b38b3a" fill="none">
          <line class="ground-line" x1="252" y1="52" x2="262" y2="428" stroke-width="2"/>
          <line class="writing-line" x1="44" y1="60" x2="50" y2="450" stroke-width="0.8" opacity="0.55"/>
          <line class="writing-line" x1="64" y1="58" x2="70" y2="450" stroke-width="0.8" opacity="0.55"/>
        </g>
      </svg>
      <div class="art-piece art-tree-1" role="img" aria-label="Gold line pine tree, drawn sideways"></div>
      <div class="art-piece art-tree-2" role="img" aria-label="Gold line pine tree, drawn sideways"></div>
      <div class="art-piece art-cabin" role="img" aria-label="Gold line log cabin with round window and smoking chimney, drawn sideways"></div>
      <div class="art-piece art-tree-3" role="img" aria-label="Gold line pine tree, drawn sideways"></div>
      <div class="art-piece art-tree-4" role="img" aria-label="Gold line pine tree, drawn sideways"></div>
    </section>
  </main>
</body>
</html>
```